Skincare Cleanser Bottle Label

New product launch of a mint facial cleanser.
Brand is called Dorvelle.
Product will be called Lunara.
Looking for a label design that can be printed using silk screening.
High gloss white plastic bottle. 8oz. White push pump top.
Clinical skincare brand, professional image, sold in medical spas.

Target Market(s)

Women Age 20-65

Industry/Entity Type

Health And Wellness

Font styles to use
Serif
Sans Serif

Requirements
Must have
• Dorvelle brand name in the orignal font.
Should not have
• Multiple colours.

```html
<!DOCTYPE html>
<html lang="en">
<head>
<meta charset="utf-8">
<title>Dorvelle Lunara Facial Cleanser Label</title>
<link rel="stylesheet" href="https://fonts.googleapis.com/css2?family=Cinzel:wght@500&family=Montserrat:wght@400;500&display=swap">
<style>
  :root {
    --label-top: #e6ded2;
    --label-mid: #f3efe9;
    --label-bottom: #fbfaf8;
    --wave-deep: #c4b190;
    --wave-light: #efe7da;
    --mint: #47c287;
    --ink: #1d1b19;
    --ink-soft: #5f5c58;
    --size-green: #5a9a1e;
  }
  * { margin: 0; padding: 0; box-sizing: border-box; }
  html, body {
    width: 1200px;
    height: 2699px;
    overflow: hidden;
    background: #ffffff;
  }
  .label {
    position: relative;
    width: 1200px;
    height: 2699px;
    background: linear-gradient(180deg, var(--label-top) 0%, var(--label-mid) 45%, var(--label-bottom) 100%);
    overflow: hidden;
  }
  .brand-name {
    position: absolute;
    top: 280px;
    left: 0;
    width: 100%;
    text-align: center;
    font-family: "Montserrat", sans-serif;
    font-weight: 400;
    font-size: 100px;
    letter-spacing: 14px;
    text-indent: 14px;
    color: var(--ink);
  }
  .wave-field {
    position: absolute;
    top: 480px;
    left: 0;
    width: 1200px;
    height: 1360px;
  }
  .flavour-badge {
    position: absolute;
    left: 345px;
    top: 1670px;
    width: 500px;
    height: 500px;
    border-radius: 50%;
    background: var(--mint);
    display: flex;
    align-items: center;
    justify-content: center;
    font-family: "Montserrat", sans-serif;
    font-weight: 400;
    font-size: 68px;
    letter-spacing: 6px;
    color: #ffffff;
  }
  .product-name {
    position: absolute;
    top: 2190px;
    left: 0;
    width: 100%;
    text-align: center;
    font-family: "Cinzel", serif;
    font-weight: 500;
    font-size: 130px;
    letter-spacing: 14px;
    color: var(--ink);
  }
  .product-type {
    position: absolute;
    top: 2365px;
    left: 0;
    width: 100%;
    text-align: center;
    font-family: "Montserrat", sans-serif;
    font-weight: 400;
    font-size: 70px;
    line-height: 92px;
    letter-spacing: 10px;
    color: var(--ink-soft);
  }
  .net-volume {
    position: absolute;
    top: 2600px;
    left: 0;
    width: 100%;
    text-align: center;
    font-family: "Montserrat", sans-serif;
    font-weight: 500;
    font-size: 48px;
    letter-spacing: 2px;
    color: var(--size-green);
  }
</style>
</head>
<body>
  <main class="label">
    <div class="brand-name">DORVELLE</div>

    <svg class="wave-field" viewBox="0 0 1200 1360" role="img" aria-label="Soft flowing cream and beige satin waves sweeping across the label">
      <defs>
        <linearGradient id="waveTone" x1="0" y1="0" x2="0" y2="1">
          <stop offset="0" stop-color="var(--wave-light)" stop-opacity="0"/>
          <stop offset="0.3" stop-color="var(--wave-deep)" stop-opacity="0.75"/>
          <stop offset="0.55" stop-color="var(--wave-light)" stop-opacity="0.9"/>
          <stop offset="0.78" stop-color="var(--wave-deep)" stop-opacity="0.6"/>
          <stop offset="1" stop-color="var(--wave-light)" stop-opacity="0"/>
        </linearGradient>
      </defs>
      <rect x="0" y="0" width="1200" height="1360" fill="url(#waveTone)"/>
    </svg>

    <div class="flavour-badge">MINT</div>

    <h1 class="product-name">LUNARA</h1>
    <p class="product-type">FACIAL<br>CLEANSER</p>
    <p class="net-volume">8oz</p>
  </main>
</body>
</html>
```